Review/Re-Design Supermarket E-Commerce website

We have launched our Supermarket E-commerce Website but feel it is lacking a modern feel.

Please re-design the current Supermarket E-commerce site, creating a more modern look and feel.

I am looking for design changes to things such as:

- Fonts
- Button shape & Size
- Shapes of boxes
- Layout of drop down menus
- A new shopping cart / button
- The Header (and in particular the use and positioning of the logo)
- Supplying a generic background image (currently berries)

Please do not change the structure of the page. For instance, the category selection will always be on the left, the items will always be displayed in rows of 3 and the shopping cart should be on the right.
Updates

Current site can be found at www.brovanmarket.com.au

Project Deadline Extended
Reason: designs coming in are generally too different from current design. we are looking for less that 10% change to the overall look and feel. one aspect that needs a lot of work is the checkout cart on the right hand side. please checkout http://www2.pelkinfreshmart.com.au/?gclid=QXRP4kdmwnLBHTYEzJuaPGEKtB

Target Market(s)

Consumers buying their weekly grocery shopping online

Industry/Entity Type

Shopping

Number of Pages Required

1 page

Requirements
Must have
• Stick to the branding of the Logo. Which is Red, Blue and White.
• Other colours may be used in small percentages.
Should not have
• Do not change the Structure of the site.

```html
<!DOCTYPE html>
<html lang="en">
<head>
<meta charset="utf-8">
<title>Brovan Market – Online Shop</title>
<link href="https://fonts.googleapis.com/css2?family=Roboto:wght@400;500;700&family=Oswald:wght@500&display=swap" rel="stylesheet">
<style>
:root{
  --blue:#1363b3;
  --blue-dark:#0d4f93;
  --red:#dd2027;
  --yellow:#f3cc10;
  --green:#1d6b2b;
  --ink:#333;
  --muted:#777;
  --footer:#2a2828;
  --footer-dark:#1f1d1d;
}
*{box-sizing:border-box;margin:0;padding:0}
html,body{width:754px;height:1200px;overflow:hidden}
body{font-family:'Roboto',sans-serif;color:var(--ink);position:relative;
  background:linear-gradient(180deg,#6b4a30 0,#a57a52 300px,#c49a70 700px,#c9a27a 1000px)}
.backdrop{position:absolute;left:0;top:0;width:754px;height:988px;
  background:linear-gradient(180deg,#5e3f28 0,#9c724b 260px,#c49a70 620px,#c9a27a 988px)}
.page{position:absolute;left:112px;top:32px;width:530px;height:956px;background:#fff}
.topbar{height:34px;background:#f3f3f3;display:flex;border-bottom:1px solid #ddd}
.phone{width:121px;background:var(--blue);color:#fff;display:flex;align-items:center;gap:10px;padding-left:14px;font-size:11px;font-weight:500}
.phone .ico{width:16px;height:16px;border-radius:50%;background:#fff;display:flex;align-items:center;justify-content:center}
.topnav{margin-left:auto;display:flex;align-items:center;font-size:7.5px;color:#777}
.topnav span{padding:0 10px;border-left:1px solid #ddd;height:33px;display:flex;align-items:center;gap:4px}
.topnav span::before{content:"";width:6px;height:6px;background:#888;border-radius:1px}
.brand{height:34px;display:flex;align-items:center;padding-left:8px;gap:6px}
.brand .name{font-size:13px;font-weight:700;color:var(--blue);letter-spacing:.3px}
.brand .mark{width:14px;height:14px;background:var(--red);border-radius:50%}
.hero{height:110px;position:relative;background:linear-gradient(180deg,#d6d2cc,#a89ea2)}
.search-band{position:absolute;left:54px;top:37px;width:422px;height:34px;background:var(--blue);display:flex;gap:8px;align-items:center;padding:0 8px}
.field{height:18px;background:#fff;font-size:7.5px;color:#666;display:flex;align-items:center;padding-left:10px;position:relative}
.field.search{width:162px}.field.filter{width:110px}.field.sort{width:118px}
.field .dd{position:absolute;right:3px;top:3px;width:12px;height:12px;background:var(--blue)}
.field .dd::after{content:"";position:absolute;left:3px;top:4px;border:3px solid transparent;border-top:4px solid #fff}
.field .mag{position:absolute;right:4px;top:4px;width:8px;height:8px;border:1.5px solid #333;border-radius:50%}
.promo{height:48px;display:flex}
.promo div{flex:1;display:flex;align-items:center;justify-content:center;gap:8px;font-family:'Oswald',sans-serif;font-size:22px;color:#fff}
.promo .specials{background:var(--red);width:264px;flex:none}
.promo .fav{background:var(--yellow)}
.promo .badge{width:26px;height:26px;border:2.5px solid #fff;border-radius:50%;display:flex;align-items:center;justify-content:center;font-size:14px}
.cats{position:absolute;left:16px;top:240px;width:100px;font-size:7px;font-weight:500}
.cats li{list-style:none;height:15.3px;display:flex;align-items:center;gap:6px}
.cats li::before{content:"";border:2px solid transparent;border-left:3px solid #555}
.cats li.open::before{border:2px solid transparent;border-top:3px solid #555;margin-top:2px}
.cats .sub{font-size:6px;font-weight:400;color:#555;height:12.6px;padding-left:2px}
.cats .sub::before{width:7px;height:7px;border:none;background:var(--blue)}
.cats .sub.on::before{box-shadow:inset 0 0 0 1.5px var(--blue),inset 0 0 0 3px #fff}
.grid-head{position:absolute;left:108px;top:243px;width:323px;height:14px;background:var(--blue);color:#fff;font-size:6px;display:flex;align-items:center;padding-left:7px}
.grid-head b{font-weight:700}
.grid-head .views{margin-left:auto;display:flex;gap:6px;padding-right:6px}
.grid-head .views i{width:7px;height:6px;border-top:1.5px solid #fff;border-bottom:1.5px solid #fff}
.grid{position:absolute;left:108px;top:258px;width:323px;display:grid;grid-template-columns:repeat(3,1fr)}
.card{height:161px;border-right:1px solid #e4e4e4;display:flex;flex-direction:column;align-items:center}
.card:nth-child(3n){border-right:none}
.card .photo{width:70px;height:66px;margin-top:14px;border-radius:4px;background:linear-gradient(180deg,#e4474a,#b81c22)}
.card .title{font-size:5.8px;font-weight:500;margin-top:18px}
.card .price{font-size:16px;font-weight:700;color:var(--blue);margin-top:1px}
.card .buy{margin-top:auto;width:100%;height:25px;background:var(--blue);display:flex;color:#fff;margin-bottom:10px}
.buy .add{width:54px;display:flex;align-items:center;justify-content:center;font-size:11px;border-right:1px solid var(--blue-dark)}
.buy .qty{flex:1;display:flex;align-items:center;justify-content:center;font-size:12px}
.buy .step{width:14px;background:var(--blue-dark);display:flex;flex-direction:column;justify-content:space-around;align-items:center}
.step i{border:3px solid transparent}
.step i.up{border-bottom:4px solid #fff;border-top:none}
.step i.dn{border-top:4px solid #fff;border-bottom:none}
.side{position:absolute;left:449px;top:244px;width:81px;color:#fff;text-align:center}
.collect{height:60px;background:var(--red);padding-top:9px}
.delivery{height:60px;background:var(--green);margin-top:1px;padding-top:14px}
.side h4{font-family:'Oswald',sans-serif;font-size:8.5px;font-weight:500;margin-top:4px}
.side small{display:block;font-size:4.5px;line-height:6px;margin-top:2px}
.cart{margin-top:3px;background:var(--blue);height:59px}
.cart .sum{display:flex;height:38px;align-items:center;justify-content:space-around;border-bottom:1px solid var(--blue-dark);font-size:5px}
.cart .sum b{display:block;font-size:12px;font-weight:500}
.cart .go{font-size:6px;font-weight:700;line-height:20px}
.pager{position:absolute;left:0;right:0;top:921px;display:flex;justify-content:center;gap:11px;font-size:6px;color:#444;align-items:center}
.pager .cur{background:var(--blue);color:#fff;padding:1px 3px;border-radius:2px}
.pager .next{background:var(--blue);color:#fff;padding:1px 5px;border-radius:2px;font-weight:700}
.footer{position:absolute;left:0;top:988px;width:754px;height:177px;background:var(--footer);color:#ccc;font-size:7px}
.footer h5{color:var(--blue);font-size:8.5px;font-weight:700;position:absolute}
.footer .badge-store{position:absolute;left:112px;width:72px;height:24px;border-radius:3px}
.footer .links{position:absolute;line-height:12.3px}
.footer .links li{list-style:none}
.footer .links li::before{content:"· "}
.card-pay{position:absolute;top:128px;width:32px;height:20px;border-radius:2px}
.email{position:absolute;left:525px;top:37px;width:115px;height:18px;background:#fff;color:#666;font-size:6px;padding-left:6px;display:flex;align-items:center}
.email b{position:absolute;right:2px;top:2px;width:14px;height:14px;background:var(--blue);color:#fff;text-align:center;line-height:14px;font-size:10px}
.social{position:absolute;top:126px;width:20px;height:20px;border:1.5px solid var(--blue);border-radius:50%}
.bottom{position:absolute;left:0;top:1165px;width:754px;height:35px;background:var(--footer-dark);color:#ddd;font-size:6px;padding:15px 0 0 114px}
</style>
</head>
<body>
<div class="backdrop" role="img" aria-label="Wooden table with bowls of red cherries at both sides"></div>

<div class="page">
  <div class="topbar">
    <div class="phone"><span class="ico"><svg width="9" height="9" viewBox="0 0 24 24"><path fill="#1363b3" d="M6.6 10.8a15 15 0 006.6 6.6l2.2-2.2c.3-.3.7-.4 1-.2 1.1.4 2.3.6 3.6.6.6 0 1 .4 1 1V20c0 .6-.4 1-1 1A17 17 0 013 4c0-.6.4-1 1-1h3.5c.6 0 1 .4 1 1 0 1.3.2 2.5.6 3.6.1.3 0 .7-.2 1z"/></svg></span>1300 555 208</div>
    <nav class="topnav"><span>Products</span><span>Login</span><span>Register</span><span>Product</span><span>My Cart</span></nav>
  </div>
  <div class="brand"><span class="name">BROVAN MARKET</span><span class="mark"></span></div>
  <div class="hero" role="img" aria-label="Fresh berries spread across a table">
    <div class="search-band">
      <div class="field search">Search<span class="mag"></span></div>
      <div class="field filter">Filter by<span class="dd"></span></div>
      <div class="field sort">Sort<span class="dd"></span></div>
    </div>
  </div>
  <div class="promo">
    <div class="specials"><span class="badge">$</span>ONLINE SPECIALS</div>
    <div class="fav"><svg width="30" height="30" viewBox="0 0 24 24"><path fill="#fff" d="M12 2l3 7 7.5.6-5.7 4.9 1.8 7.4L12 18l-6.6 3.9 1.8-7.4L1.5 9.6 9 9z"/></svg>FAVOURITES</div>
  </div>

  <ul class="cats">
    <li class="open">Baby</li>
    <li class="sub on">accessories</li><li class="sub">baby food</li><li class="sub">baby oil</li><li class="sub">bath time</li><li class="sub">change time</li><li class="sub">cleaning</li><li class="sub">creams &amp; ointments</li><li class="sub">feeding time</li><li class="sub">formula</li>
    <li>Barkey</li><li>Baking Needs</li><li>Biscuits</li><li>Breakfast Foods</li><li>Canned Food</li><li>Cheese</li><li>Chilled Foods</li><li>Chips</li><li>Condiments</li><li>Confedtionery</li><li>Cooking Needs, Seaso</li><li>Desserts</li><li>Frozen Food</li><li>Fruit</li><li>Hardware &amp; Outdoor</li><li>Health Foods</li><li>Homewares</li><li>Household Cleaning</li><li>International Foods</li><li>Jams &amp; Spreads</li><li>Laundry</li><li>Meat</li><li>Milk</li>
  </ul>

  <div class="grid-head"><b>Baby</b>&nbsp;/ Accessories<span class="views"><i></i><i></i><i></i><i></i></span></div>
  <div class="grid">
    <div class="card"><div class="photo" role="img" aria-label="Bag of red apples"></div><div class="title">Apples Red 2kg Bag</div><div class="price">$8.39</div><div class="buy"><span class="add">Add</span><span class="qty">1</span><span class="step"><i class="up"></i><i class="dn"></i></span></div></div>
    <div class="card"><div class="photo" role="img" aria-label="Bag of red apples"></div><div class="title">Apples Red 2kg Bag</div><div class="price">$8.39</div><div class="buy"><span class="add">Add</span><span class="qty">1</span><span class="step"><i class="up"></i><i class="dn"></i></span></div></div>
    <div class="card"><div class="photo" role="img" aria-label="Bag of red apples"></div><div class="title">Apples Red 2kg Bag</div><div class="price">$8.39</div><div class="buy"><span class="add">Add</span><span class="qty">1</span><span class="step"><i class="up"></i><i class="dn"></i></span></div></div>
    <div class="card"><div class="photo" role="img" aria-label="Bag of red apples"></div><div class="title">Apples Red 2kg Bag</div><div class="price">$8.39</div><div class="buy"><span class="add">Add</span><span class="qty">1</span><span class="step"><i class="up"></i><i class="dn"></i></span></div></div>
    <div class="card"><div class="photo" role="img" aria-label="Bag of red apples"></div><div class="title">Apples Red 2kg Bag</div><div class="price">$8.39</div><div class="buy"><span class="add">Add</span><span class="qty">1</span><span class="step"><i class="up"></i><i class="dn"></i></span></div></div>
    <div class="card"><div class="photo" role="img" aria-label="Bag of red apples"></div><div class="title">Apples Red 2kg Bag</div><div class="price">$8.39</div><div class="buy"><span class="add">Add</span><span class="qty">1</span><span class="step"><i class="up"></i><i class="dn"></i></span></div></div>
    <div class="card"><div class="photo" role="img" aria-label="Bag of red apples"></div><div class="title">Apples Red 2kg Bag</div><div class="price">$8.39</div><div class="buy"><span class="add">Add</span><span class="qty">1</span><span class="step"><i class="up"></i><i class="dn"></i></span></div></div>
    <div class="card"><div class="photo" role="img" aria-label="Bag of red apples"></div><div class="title">Apples Red 2kg Bag</div><div class="price">$8.39</div><div class="buy"><span class="add">Add</span><span class="qty">1</span><span class="step"><i class="up"></i><i class="dn"></i></span></div></div>
    <div class="card"><div class="photo" role="img" aria-label="Bag of red apples"></div><div class="title">Apples Red 2kg Bag</div><div class="price">$8.39</div><div class="buy"><span class="add">Add</span><span class="qty">1</span><span class="step"><i class="up"></i><i class="dn"></i></span></div></div>
    <div class="card"><div class="photo" role="img" aria-label="Bag of red apples"></div><div class="title">Apples Red 2kg Bag</div><div class="price">$8.39</div><div class="buy"><span class="add">Add</span><span class="qty">1</span><span class="step"><i class="up"></i><i class="dn"></i></span></div></div>
    <div class="card"><div class="photo" role="img" aria-label="Bag of red apples"></div><div class="title">Apples Red 2kg Bag</div><div class="price">$8.39</div><div class="buy"><span class="add">Add</span><span class="qty">1</span><span class="step"><i class="up"></i><i class="dn"></i></span></div></div>
    <div class="card"><div class="photo" role="img" aria-label="Bag of red apples"></div><div class="title">Apples Red 2kg Bag</div><div class="price">$8.39</div><div class="buy"><span class="add">Add</span><span class="qty">1</span><span class="step"><i class="up"></i><i class="dn"></i></span></div></div>
  </div>

  <aside class="side">
    <div class="collect"><svg width="12" height="12" viewBox="0 0 24 24"><path fill="#fff" d="M3 3l17 7-7 2-2 7z"/></svg><h4>CLICK&amp;COLLECT</h4><small>12/40 HARBOUR ROAD<br>KELBY TAS 7290</small></div>
    <div class="delivery"><svg width="32" height="18" viewBox="0 0 32 18"><rect x="1" y="1" width="19" height="11" fill="none" stroke="#fff" stroke-width="2"/><path d="M21 5h6l4 4v3h-10z" fill="#fff"/><circle cx="7" cy="15" r="2.5" fill="#fff"/><circle cx="26" cy="15" r="2.5" fill="#fff"/></svg><h4>DELIVERY INFO</h4></div>
    <div class="cart">
      <div class="sum"><span><svg width="12" height="9" viewBox="0 0 12 9"><path d="M0 1h2l1 6h7l1-5H3" fill="none" stroke="#fff" stroke-width="1.4"/></svg><br>0 ITEMS</span><span>SUB TOTAL<b>$0.00</b></span></div>
      <div class="go">CHECKOUT</div>
    </div>
  </aside>

  <div class="pager"><span>← Prev</span><span>1</span><span class="cur">2</span><span>3</span><span>4</span><span>...</span><span>10</span><span>20</span><span>30</span><span class="next">Next →</span></div>
</div>

<footer class="footer">
  <h5 style="left:115px;top:17px">DOWNLOAD OUR APP</h5>
  <div class="badge-store" style="top:44px;background:#111;border:1px solid #444"></div>
  <div class="badge-store" style="top:77px;background:#8bbf3c"></div>
  <h5 style="left:115px;top:113px">WE ACCEPT</h5>
  <div class="card-pay" style="left:113px;background:#e8e8e8"></div>
  <div class="card-pay" style="left:150px;background:#fff"></div>

  <h5 style="left:251px;top:17px">ONLINE</h5>
  <ul class="links" style="left:251px;top:44px"><li>My Account</li><li>My Past Orders</li><li>Online Specials</li><li>Everyday Specials</li></ul>
  <ul class="links" style="left:345px;top:44px"><li>Delivery</li><li>FAQ</li><li>Privacy Policy</li><li>Terms &amp; Conditions</li></ul>
  <ul class="links" style="left:435px;top:44px"><li>End User License</li><li>Agreement</li></ul>
  <ul class="links" style="left:251px;top:106px"><li>About Kartly</li><li>About Us</li></ul>
  <ul class="links" style="left:345px;top:106px"><li>Contact us</li><li>1300 555 208</li></ul>

  <h5 style="left:525px;top:17px">NEWSLETTER</h5>
  <div class="email">Email Address<b>+</b></div>
  <h5 style="left:525px;top:101px">KEEP IN TOUCH</h5>
  <span class="social" style="left:525px"></span><span class="social" style="left:549px"></span><span class="social" style="left:572px"></span>
</footer>
<div class="bottom">© 2015 <b>BROVAN</b>. ALL RIGHTS RESERVED.</div>
</body>
</html>
```